Poster Design Project

Need a design for a music festival called Counter-Lanternweek

The design needs to have areas for the following:
- Band Names
- DJ Names
- Sponsor Names and Logos
- Event location, Date & Time

Industry/Entity Type

Festival

```html
<!DOCTYPE html>
<html lang="en">
<head>
<meta charset="utf-8">
<title>Counter-Lanternweek Music Festival</title>
<link rel="stylesheet" href="https://fonts.googleapis.com/css2?family=Source+Sans+3:wght@600&display=swap">
<style>
  :root {
    --festival-yellow: #ecf72e;
    --festival-blue: #1a3be8;
    --artwork-light: #f8fbd8;
    --artwork-mid: #f3f8b0;
    --badge-white: #ffffff;
  }
  html, body {
    margin: 0;
    padding: 0;
    overflow: hidden;
    background: var(--festival-yellow);
  }
  .poster {
    width: 1000px;
    height: 1200px;
    position: relative;
    overflow: hidden;
    background: var(--festival-yellow);
    font-family: "Source Sans 3", sans-serif;
    font-weight: 600;
  }
  .poster-art {
    position: absolute;
    inset: 0;
    width: 1000px;
    height: 1200px;
  }
  .title-text {
    fill: var(--festival-blue);
    font-family: "Source Sans 3", sans-serif;
    font-weight: 600;
    font-size: 142px;
    letter-spacing: -2px;
  }
  .subtitle-text {
    fill: var(--festival-blue);
    font-family: "Source Sans 3", sans-serif;
    font-weight: 600;
    font-size: 42px;
  }
  .lineup-text {
    fill: var(--festival-blue);
    font-family: "Source Sans 3", sans-serif;
    font-weight: 600;
    font-size: 19px;
  }
  .sponsor-text {
    fill: var(--festival-blue);
    font-family: "Source Sans 3", sans-serif;
    font-weight: 600;
    font-size: 17px;
  }
  .logo-badge { fill: var(--badge-white); }
  .logo-text {
    fill: var(--festival-blue);
    font-family: "Source Sans 3", sans-serif;
    font-weight: 600;
    font-size: 19px;
  }
</style>
</head>
<body>
<main class="poster">
  <svg class="poster-art" viewBox="0 0 1000 1200" xmlns="http://www.w3.org/2000/svg">
    <defs>
      <linearGradient id="artwork-fill" x1="0" y1="0" x2="1" y2="0">
        <stop offset="0" stop-color="var(--artwork-mid)"/>
        <stop offset="1" stop-color="var(--artwork-light)"/>
      </linearGradient>
    </defs>

    <rect class="artwork-area" role="img"
      aria-label="Illustration: a large saxophone composed of small white musical instrument drawings"
      x="-430" y="-95" width="860" height="190" rx="95"
      fill="url(#artwork-fill)"
      transform="translate(520 480) rotate(-38)"/>

    <g class="festival-title">
      <text class="title-text" transform="translate(80 690) rotate(-35.4)">Counter</text>
      <text class="title-text" transform="translate(268 782) rotate(-35.4)">Lanternweek</text>
    </g>

    <text class="subtitle-text" transform="translate(112 718) rotate(57)">Music Festival</text>

    <g class="lineup">
      <text class="lineup-text" transform="translate(400 765) rotate(-35.4)">Band Name</text>
      <text class="lineup-text" transform="translate(417 792) rotate(-35.4)">DJ Name</text>
      <text class="lineup-text" transform="translate(435 821) rotate(-35.4)">Location</text>
      <text class="lineup-text" transform="translate(457 850) rotate(-35.4)">Date &amp; Time</text>
    </g>

    <g class="sponsors">
      <text class="sponsor-text" x="435" y="1152">Sponsor Name</text>
      <text class="sponsor-text" x="581" y="1152">Sponsor Name</text>
      <text class="sponsor-text" x="727" y="1152">Sponsor Name</text>
      <circle class="logo-badge" cx="918" cy="1142" r="43"/>
      <text class="logo-text" x="918" y="1148" text-anchor="middle">Logo</text>
    </g>
  </svg>
</main>
</body>
</html>
```